Velmora Care! Create an exciting flyer for our hemodialysis clinic

Create an engaging Flyer that shows our offering and that will drive patients to our hemodialysis clinic. www.velmoracare.example

Target Market(s)

Mass public

Industry/Entity Type

Healthcare

Requirements
Must have
• 1 Our logo. 2. Should include that we accept all insurances 3. Our tag line “Transforming Lives, One Dialysis Session at a Time.”

```html
<!DOCTYPE html>
<html lang="en">
<head>
<meta charset="utf-8">
<title>Velmora Care – In-Center Hemodialysis Flyer</title>
<link rel="stylesheet" href="https://fonts.googleapis.com/css2?family=Lato:wght@400;700;900&family=Montserrat:wght@400;500;600;700;800&display=swap">
<style>
  :root {
    --backdrop: #5f5f5f;
    --green: #65a844;
    --green-bright: #0aa64a;
    --blue: #4475bb;
    --navy: #1d3f8a;
    --ink: #2d2d2d;
    --white: #ffffff;
    --mist: #eef0f1;
  }
  * { margin: 0; padding: 0; box-sizing: border-box; }
  html, body { width: 1200px; height: 2192px; overflow: hidden; background: var(--backdrop); }
  .flyer {
    position: absolute; left: 40px; top: 371px;
    width: 1120px; height: 1449px;
    background: var(--white); overflow: hidden;
    font-family: "Montserrat", sans-serif; color: var(--ink);
    box-shadow: 0 20px 50px rgba(0,0,0,.35);
  }
  .hero-photo {
    position: absolute; left: 0; top: 0; width: 1120px; height: 900px;
    background: linear-gradient(90deg, #1f8d49 0%, #3a9a63 35%, #7da39a 65%, #b9c3c9 100%);
  }
  .shapes { position: absolute; left: 0; top: 0; }
  .headline {
    position: absolute; left: 79px; font-family: "Lato", sans-serif;
    font-weight: 900; color: var(--white); line-height: 1; letter-spacing: -1px;
    white-space: nowrap;
  }
  .headline--first { top: 248px; font-size: 124px; }
  .lives-pill {
    position: absolute; left: 0; top: 358px; width: 428px; height: 113px;
    background: var(--green-bright); border-radius: 0 57px 57px 0;
  }
  .headline--second { top: 365px; font-size: 124px; }
  .tagline {
    position: absolute; left: 79px; top: 508px;
    font-family: "Lato", sans-serif; font-weight: 400; font-size: 58px;
    line-height: 62px; color: var(--white);
  }
  .insurance-badge { position: absolute; left: 894px; top: 80px; }
  .brand-seal {
    position: absolute; left: 678px; top: 471px; width: 312px; height: 312px;
    border-radius: 50%; background: var(--white);
    box-shadow: 0 8px 24px rgba(0,0,0,.25);
    display: flex; align-items: center; justify-content: center;
  }
  .brand-seal::before {
    content: ""; position: absolute; inset: 14px; border-radius: 50%;
    border: 4px solid var(--blue);
  }
  .brand-name {
    font-family: "Montserrat", sans-serif; font-weight: 700; font-size: 40px;
    color: var(--blue); text-align: center; line-height: 1.1; letter-spacing: 1px;
  }
  .service-icon {
    position: absolute; left: 122px; top: 793px; width: 124px; height: 124px;
    border-radius: 50%; border: 3px solid var(--blue); background: #f4f7fc;
  }
  .service-title {
    position: absolute; left: 271px; top: 790px;
    font-weight: 800; font-size: 68px; line-height: 62px; letter-spacing: -1px;
    white-space: nowrap;
  }
  .service-title .line-green { color: var(--green); display: block; }
  .service-title .line-blue { color: var(--blue); display: block; }
  .details {
    position: absolute; left: 79px; top: 942px; width: 980px;
    border-left: 5px solid var(--blue); padding-left: 22px;
    font-size: 26px; line-height: 34px; font-weight: 500;
  }
  .details p + p { margin-top: 13px; }
  .details .hl { color: var(--blue); font-weight: 600; }
  .network-band {
    position: absolute; left: 0; top: 1192px; width: 1120px; height: 100px;
    background: var(--green); color: var(--white);
    padding: 24px 0 0 79px; font-size: 24px; line-height: 31px; font-weight: 400;
  }
  .network-band strong { font-weight: 700; }
  .contact-band {
    position: absolute; left: 0; top: 1292px; width: 1120px; height: 157px;
    background: var(--blue);
  }
  .contact-band .bottom-curve { position: absolute; left: 0; top: 0; }
  .call-pill {
    position: absolute; left: 79px; top: 24px; width: 287px; height: 50px;
    background: var(--green); border-radius: 25px; color: var(--white);
  }
  .call-pill .phone-disc {
    position: absolute; left: 29px; top: -6px; width: 62px; height: 62px;
    border-radius: 50%; background: var(--white); border: 3px solid var(--green);
    display: flex; align-items: center; justify-content: center;
  }
  .call-pill .call-label {
    position: absolute; left: 110px; top: 2px; font-size: 27px; font-weight: 600;
    white-space: nowrap;
  }
  .call-pill .call-note {
    position: absolute; left: 120px; top: 33px; font-size: 12px; font-weight: 400;
    white-space: nowrap;
  }
  .phone-number {
    position: absolute; left: 382px; top: 20px; font-size: 42px; font-weight: 600;
    color: var(--white); white-space: nowrap;
  }
  .divider { position: absolute; left: 711px; top: 24px; width: 2px; height: 54px; background: var(--white); }
  .website { position: absolute; left: 732px; top: 22px; white-space: nowrap; }
  .website .label { color: var(--green); font-size: 22px; font-weight: 500; display: block; }
  .website .url { color: var(--white); font-size: 23px; font-weight: 600; display: block; }
</style>
</head>
<body>
<main class="flyer">
  <div class="hero-photo" role="img" aria-label="Photo of a nurse with a stethoscope caring for a patient resting in a treatment chair, tinted green"></div>

  <svg class="shapes" width="1120" height="1000" viewBox="0 0 1120 1000" aria-hidden="true">
    <defs>
      <linearGradient id="band-blue" x1="0" y1="0" x2="1" y2="0">
        <stop offset="0" stop-color="#1d3f8a"/>
        <stop offset="1" stop-color="#4475bb"/>
      </linearGradient>
      <linearGradient id="band-green" x1="0" y1="0" x2="1" y2="0">
        <stop offset="0" stop-color="#0f7d4a"/>
        <stop offset="1" stop-color="#65a844"/>
      </linearGradient>
    </defs>
    <path d="M0 760 C380 700 760 600 1120 460 L1120 500 C760 640 380 735 0 790 Z" fill="url(#band-green)"/>
    <path d="M0 790 C380 735 760 640 1120 500 L1120 580 C760 700 380 790 0 845 Z" fill="url(#band-blue)"/>
    <path d="M0 845 C380 790 760 700 1120 580 L1120 1000 L0 1000 Z" fill="#ffffff"/>
    <polygon points="1030,560 1120,520 1120,640 930,820 860,760" fill="#eef0f1"/>
  </svg>

  <div class="lives-pill"></div>
  <h1 class="headline headline--first">Transforming</h1>
  <div class="headline headline--second">Lives</div>
  <p class="tagline">One Dialysis Session<br>at a Time</p>

  <svg class="insurance-badge" width="150" height="150" viewBox="0 0 150 150" role="img" aria-label="We accept all insurance">
    <defs>
      <path id="badge-arc-top" d="M28 75 A47 47 0 0 1 122 75"/>
      <path id="badge-arc-bottom" d="M24 75 A51 51 0 0 0 126 75"/>
    </defs>
    <circle cx="75" cy="75" r="74" fill="#4475bb"/>
    <circle cx="75" cy="75" r="64" fill="none" stroke="#ffffff" stroke-width="2"/>
    <circle cx="75" cy="75" r="32" fill="none" stroke="#ffffff" stroke-width="2"/>
    <path d="M60 75 L71 87 L92 60" fill="none" stroke="#ffffff" stroke-width="7" stroke-linecap="round" stroke-linejoin="round"/>
    <text font-family="Montserrat, sans-serif" font-size="13" font-weight="700" fill="#ffffff" letter-spacing="1.5">
      <textPath href="#badge-arc-top" startOffset="50%" text-anchor="middle">WE ACCEPT ALL</textPath>
    </text>
    <text font-family="Montserrat, sans-serif" font-size="13" font-weight="700" fill="#ffffff" letter-spacing="1.5" dy="10">
      <textPath href="#badge-arc-bottom" startOffset="50%" text-anchor="middle">INSURANCE</textPath>
    </text>
  </svg>

  <div class="brand-seal">
    <div class="brand-name">VELMORA<br>CARE</div>
  </div>

  <div class="service-icon" role="img" aria-label="Dialysis machine icon"></div>
  <h2 class="service-title">
    <span class="line-green">IN-CENTER</span>
    <span class="line-blue">HEMODIALYSIS</span>
  </h2>

  <section class="details">
    <p>We offer <span class="hl">In-center hemodialysis</span> for renal patients who prefer to have their treatments at a dialysis center.</p>
    <p>Our dialysis center has <span class="hl">6 Kelvane Dialysis Machines</span>, supported by our state of the art water purification system.</p>
    <p><span class="hl">Pick up and drop off</span> of patients is an additional service we offer for all in-center hemodialysis patients.</p>
  </section>

  <div class="network-band">
    Once you’re a dialysis patient with Velmora Care, you can also dialyze at any or our<br>
    partner locations in <strong>Trinidad (Chaguanas and Piarco)</strong>
  </div>

  <footer class="contact-band">
    <svg class="bottom-curve" width="1120" height="157" viewBox="0 0 1120 157" aria-hidden="true">
      <path d="M204 157 C220 130 240 116 290 116 L1120 116 L1120 157 Z" fill="#ffffff"/>
    </svg>
    <div class="call-pill">
      <span class="phone-disc">
        <svg width="32" height="32" viewBox="0 0 24 24" aria-hidden="true">
          <path d="M6.6 10.8a15.2 15.2 0 0 0 6.6 6.6l2.2-2.2a1 1 0 0 1 1-.25 11.4 11.4 0 0 0 3.6.57 1 1 0 0 1 1 1V20a1 1 0 0 1-1 1A17 17 0 0 1 3 4a1 1 0 0 1 1-1h3.5a1 1 0 0 1 1 1c0 1.25.2 2.45.57 3.57a1 1 0 0 1-.25 1z" fill="#65a844"/>
        </svg>
      </span>
      <span class="call-label">Call us now</span>
      <span class="call-note">for more information!</span>
    </div>
    <div class="phone-number">868-555-0142</div>
    <div class="divider"></div>
    <div class="website">
      <span class="label">Visit Our Website:</span>
      <span class="url">www.velmoracare.example</span>
    </div>
  </footer>
</main>
</body>
</html>
```